Business card for a plastic surgeon

i need a business card for a plastic surgeon. I have two adresses. The card should communicate safety, simmetry, beauty and with soft colors.
What i want in the card:
- my logo: Letters "R"and "T" (picture uploaded)
- my name: Rodrigo Tavernelli
- my registration: CRM 527 319
- my adresses and phone numbers (2):
- Av Dr Bento Arruda, 2730, sala 408 - Vila Olímpia | São Paulo/ SP - Phone: 11 4721-6350
- Al. Itaquera, 61, 3 andar - Alphaville | Barueri/ SP - Phone: 11 5038-2917

- my social network: site, facebook and instagram

Target Market(s)

people (95% girls and women) that want cosmetic procedures and plastic surgery

Industry/Entity Type

Business

Contact Information for Business Card

The card should communicate safety, simmetry, beauty and with soft colors.
Beige, brown, gray, rosy are some options. Color is free

Font styles to use
Serif

Requirements
Must have
• - my logo: Letters "R"and "T" (picture uploaded)
• - my name: Rodrigo Tavernelli
• - my registration: CRM 527 319
• - my adresses and phone numbers (2):
• - Av Dr Bento Arruda, 2730, sala 408 - Vila Olímpia | São Paulo/ SP - Phone: 11 4721-6350
• - Al. Itaquera, 61, 3 andar - Alphaville | Barueri/ SP - Phone: 11 5038-2917
• - my social network: site, facebook and instagram
Should not have
• other images (only my logo)

```html
<!DOCTYPE html>
<html lang="pt-BR">
<head>
<meta charset="utf-8">
<title>Rodrigo Tavernelli – Cartão de visita</title>
<link rel="stylesheet" href="https://fonts.googleapis.com/css2?family=Cinzel:wght@400;700&family=Tinos:wght@400;700&display=swap">
<style>
  :root {
    --backdrop: #2d2d2d;
    --taupe: #a38a71;
    --paper: #ffffff;
    --ink: #6f6f6f;
    --rule: #9a9a9a;
    --on-taupe: #ffffff;
  }
  * { margin: 0; padding: 0; box-sizing: border-box; }
  html, body { width: 1200px; height: 900px; overflow: hidden; background: var(--backdrop); }
  .canvas { position: relative; width: 1200px; height: 900px; }

  .card {
    position: absolute; top: 193px; width: 297px; height: 513px;
    border-radius: 26px; overflow: hidden;
  }
  .card--front { left: 275px; background: var(--taupe); color: var(--on-taupe); text-align: center; }
  .card--back { left: 629px; background: var(--paper); color: var(--ink); font-family: "Tinos", "Times New Roman", serif; }

  .front-mark {
    position: absolute; top: 200px; left: 0; right: 0;
    font-family: "Cinzel", serif; font-size: 30px; font-weight: 400; letter-spacing: 2px;
    color: var(--on-taupe);
  }
  .front-name {
    position: absolute; top: 398px; left: 0; right: 0;
    font-family: "Cinzel", serif; font-size: 20px; letter-spacing: 0.5px; font-weight: 400;
  }
  .front-title {
    position: absolute; top: 426px; left: 0; right: 0;
    font-family: "Cinzel", serif; font-size: 11px; letter-spacing: 3.2px;
  }

  .back-mark {
    position: absolute; top: 100px; right: 34px;
    font-family: "Tinos", serif; font-size: 16px; color: var(--taupe); letter-spacing: 1px;
  }
  .contact { position: absolute; left: 44px; width: 219px; }
  .contact-row { display: flex; align-items: flex-start; font-size: 14px; line-height: 16.5px; }
  .contact-row svg { flex: 0 0 11px; width: 11px; height: 11px; margin: 2px 7px 0 0; fill: var(--ink); }
  .identity { top: 229px; }
  .identity .name { font-weight: 700; color: var(--taupe); font-size: 14.5px; letter-spacing: 0.3px; }
  .identity .crm { font-size: 10.5px; margin-left: 18px; line-height: 12px; }
  .rule { position: absolute; left: 44px; width: 219px; height: 1px; background: var(--rule); }
  .office-1 { top: 275px; }
  .office-2 { top: 361px; }
  .online { top: 446px; }
</style>
</head>
<body>
<main class="canvas">
  <section class="card card--front">
    <div class="front-mark">Tavernelli</div>
    <h1 class="front-name">DR. RODRIGO TAVERNELLI</h1>
    <p class="front-title">CIRURGIÃO PLÁSTICO</p>
  </section>

  <section class="card card--back">
    <div class="back-mark">Tavernelli</div>

    <div class="contact identity">
      <div class="contact-row name">
        <svg viewBox="0 0 12 12"><rect x="0" y="0" width="12" height="12" rx="2.5"/><circle cx="6" cy="4.5" r="2" fill="#fff"/><path d="M2.5 10.5c0-2 1.6-3.2 3.5-3.2s3.5 1.2 3.5 3.2z" fill="#fff"/></svg>
        RODRIGO TAVERNELLI
      </div>
      <div class="crm">CRM 527 319</div>
    </div>
    <div class="rule" style="top:267px"></div>

    <div class="contact office-1">
      <div class="contact-row">
        <svg viewBox="0 0 12 12"><path d="M6 0a4 4 0 0 0-4 4c0 3 4 8 4 8s4-5 4-8a4 4 0 0 0-4-4zm0 5.6a1.6 1.6 0 1 1 0-3.2 1.6 1.6 0 0 1 0 3.2z"/></svg>
        <span>Av Dr Bento Arruda, 2730<br>sala 408 - Vila Olímpia<br>São Paulo/ SP</span>
      </div>
      <div class="contact-row">
        <svg viewBox="0 0 12 12"><path d="M0 5.5C1.5 3 10.5 3 12 5.5L11 7.5 8.5 7 8 5.5C7 5 5 5 4 5.5L3.5 7 1 7.5z"/><rect x="3" y="7.5" width="6" height="3" rx="1"/></svg>
        11 4721-6350
      </div>
    </div>
    <div class="rule" style="top:352px"></div>

    <div class="contact office-2">
      <div class="contact-row">
        <svg viewBox="0 0 12 12"><path d="M6 0a4 4 0 0 0-4 4c0 3 4 8 4 8s4-5 4-8a4 4 0 0 0-4-4zm0 5.6a1.6 1.6 0 1 1 0-3.2 1.6 1.6 0 0 1 0 3.2z"/></svg>
        <span>Al. Itaquera, 61, 3 andar<br>Alphaville<br>Barueri/ SP</span>
      </div>
      <div class="contact-row">
        <svg viewBox="0 0 12 12"><path d="M0 5.5C1.5 3 10.5 3 12 5.5L11 7.5 8.5 7 8 5.5C7 5 5 5 4 5.5L3.5 7 1 7.5z"/><rect x="3" y="7.5" width="6" height="3" rx="1"/></svg>
        11 5038-2917
      </div>
    </div>
    <div class="rule" style="top:438px"></div>

    <div class="contact online">
      <div class="contact-row">
        <svg viewBox="0 0 12 12"><circle cx="6" cy="6" r="5.4" fill="none" stroke="#6f6f6f" stroke-width="1.1"/><ellipse cx="6" cy="6" rx="2.3" ry="5.4" fill="none" stroke="#6f6f6f" stroke-width="1"/><path d="M0.8 4.2h10.4M0.8 7.8h10.4" stroke="#6f6f6f" stroke-width="1"/></svg>
        tavernelliplastica.br
      </div>
      <div class="contact-row">
        <svg viewBox="0 0 12 12"><rect x="0.5" y="0.5" width="11" height="11" rx="2"/></svg>
        rodrigotavernelli
      </div>
      <div class="contact-row">
        <svg viewBox="0 0 12 12"><circle cx="6" cy="6" r="5.5"/></svg>
        rodrigotavernelli
      </div>
    </div>
  </section>
</main>
</body>
</html>
```